Mentorloft needs a WordPress - Design

I am a personal, team and business coach and help my clients to develop their potential. I mainly work with individuals and teams, but this can also be in the context of a company.
My business is called "Mentorloft"

The main goal of this website is to promote my business and to attire new customers.
I also want to present my concepts and ideas about coaching and how I actually do coaching and consulting. This is also to inform potential customers what coaching actually is and what it's not.
I want to host this website on a hosting-provider and want to be able to add and adapt content on my own. I'm thus looking for a WordPress - design.

Content:

vision
• Why do I do this
• How do I do this
• What am I doing

Coaching
• Career development
• Conflicts
• What is coaching, why coaching
• Conduct of a session and of the whole consultation
Limits of coaching
• Examples of positive effects of coaching

Support concept

Blog about current topics

Left

About me

Contact form

Footer / disclaimer

The following topics are the most important parts of my daily work as a coach with my clients, maybe this helps to get choos a suitable design:
- personality development, analyzing aspects and patterns and showing their influence
- Improve collaboration and cooperation in teams
- Addressing and solving conflicts (private and business)
- Identify and foster motivation, drivers, goals and action patterns
- Define next steps for the further improvement
- Accompany reorientation in professional career
- Discovering and using the strengths of the customers

The major part of my work is direct conversation with the customer, on site or virtually. My job is to support the customer in recognizing his own ideas, goals and possibilities and to define next steps in the desired direction

Target Market(s)

Small businesses and private persons in serch of a professional coach

Industry/Entity Type

Consultant

Number of Pages Required

1 page

Font styles to use
Sans Serif

Requirements
Must have
• - Logo / Name (see attachment)
- Menu, fixed navigation
- content
- blog
- Footer (contact, disclaimer)

- I need a WordPress design suitable for Mobile and Desktop devices.
- I'm looking for a modern, friendly and easy to use web site.
- First page as Long-pager (scrolling), other pages as long-pager or standard
- Decent, friendly colors but still clear, simple
Nice to have
• - Panorama image (image changing on every load of the site)
- Quote (changing on every load of the site)

```html
<!DOCTYPE html>
<html lang="en">
<head>
<meta charset="utf-8">
<title>Mentorloft — Coaching</title>
<link rel="stylesheet" href="https://fonts.googleapis.com/css2?family=Poppins:wght@300;400;500;600&family=Prata&display=swap">
<style>
:root{
  --accent:#1bb5ec;
  --navy:#1f2d7a;
  --ink:#1c1c1c;
  --muted:#777;
  --panel:#ececec;
  --soft:#f4f4f4;
  --footer:#0f1b2c;
  --line:#d9d9d9;
  --serif:"Prata",Georgia,serif;
  --sans:"Poppins",Arial,sans-serif;
}
*{box-sizing:border-box;margin:0;padding:0}
html,body{width:1200px;height:4199px;overflow:hidden}
body{position:relative;font-family:var(--sans);color:var(--ink);background:#fff}
.abs{position:absolute}
.btn{position:absolute;background:var(--accent);color:#fff;font:500 11px var(--sans);letter-spacing:.5px;display:flex;align-items:center;justify-content:center;text-transform:uppercase}
.eyebrow{font:400 15px var(--sans);letter-spacing:4px;text-transform:uppercase}
.rule{position:absolute;height:3px;width:80px;background:var(--ink)}
.serif{font-family:var(--serif);font-weight:400}
.center{left:0;width:1200px;text-align:center}
.body-text{font:300 11px/19px var(--sans);color:var(--muted)}

/* nav */
.nav{position:absolute;top:0;left:0;width:1200px;height:60px;background:#fff}
.nav a{position:absolute;top:24px;font:400 10.5px var(--sans);letter-spacing:.6px;color:#333;text-decoration:none}
.nav a.active{color:var(--accent)}
.nav-brand{position:absolute;left:541px;top:0;width:118px;height:90px;background:#fff;z-index:3;display:flex;flex-direction:column;align-items:center;justify-content:flex-end;padding-bottom:14px;gap:10px}
.nav-brand .mark{width:26px;height:26px;background:var(--navy)}
.nav-brand span{font:500 10.5px var(--sans);letter-spacing:1.5px;color:var(--accent)}

/* hero */
.hero{top:60px;left:0;width:1200px;height:555px;background:linear-gradient(180deg,#3a3f45 0%,#8a6a3e 35%,#c79a55 50%,#6e5434 72%,#2c2218 100%)}
.dots{top:580px;left:558px;display:flex;gap:9px}
.dots i{width:9px;height:9px;border-radius:50%;background:rgba(255,255,255,.5)}
.dots i:first-child{background:#fff}

/* about */
.about-photo{left:150px;top:691px;width:354px;height:364px;background:linear-gradient(160deg,#d9dcd6,#a79a80 60%,#6f6a5e);z-index:2}
.about-panel{left:443px;top:760px;width:607px;height:362px;background:var(--panel)}

/* services */
.services{top:1294px;left:0;width:1200px;height:374px;border-top:1px solid var(--line)}
.card{position:absolute;top:0;width:300px;height:374px;border-right:1px solid var(--line);text-align:center}
.card.active{border-top:3px solid var(--accent);border-left:1px solid var(--accent);border-right:1px solid var(--accent);top:-1px}
.card svg{margin-top:45px}
.card h3{margin-top:22px;font:500 14px/18px var(--sans);letter-spacing:1.5px;text-transform:uppercase}
.card p{width:230px;margin:14px auto 0}
.plus{width:24px;height:24px;border-radius:50%;background:var(--accent);color:#fff;margin:18px auto 0;font:400 18px/24px var(--sans)}

/* banner */
.banner{top:1668px;left:0;width:1200px;height:414px;background:linear-gradient(120deg,#3a2a1c 0%,#6b4522 45%,#2e2117 70%,#1c140e 100%)}

/* blog */
.blog-img{position:absolute;width:262px}
.blog-card{position:absolute;width:244px;border:2px solid #dcdcdc;background:#fff;padding:16px 14px}
.blog-card h4{font:600 11px/14px var(--sans)}
.blog-card .date{font:400 10px var(--sans);margin-top:10px}
.blog-card p{font:300 10px/15px var(--sans);color:var(--muted);margin-top:10px}
.blog-card a{display:block;margin-top:10px;font:400 9px var(--sans);color:var(--accent)}

/* case study */
.case{top:2805px;left:0;width:1200px;height:561px;background:linear-gradient(180deg,#c6ccd6 0%,#dfe3e9 40%,#b8c3d2 100%)}
.case-panel{left:150px;top:2939px;width:546px;height:337px;background:rgba(240,240,240,.96);padding:60px 36px}
.case-photo{left:696px;top:2870px;width:354px;height:364px;background:linear-gradient(170deg,#e6e2dc,#9a8f82 55%,#4b4038)}

/* contact */
.contact-side{top:3366px;left:0;width:450px;height:447px;background:var(--soft)}
.brand-line{display:flex;align-items:center;gap:10px;font:500 22px var(--sans);letter-spacing:2px;color:var(--accent)}
.brand-line i{width:22px;height:22px;background:var(--navy)}
.info-label{font:400 9.5px var(--sans);color:#444}
.info-val{font:400 14px var(--sans);color:var(--accent);text-decoration:underline}
.field{position:absolute;height:23px;border-bottom:1px solid var(--line);font:400 11px var(--sans);color:#555;padding-left:14px}

/* footer */
.footer{top:3813px;left:0;width:1200px;height:386px;background:var(--footer);color:#fff}
.footer h5{position:absolute;top:76px;font:500 11px var(--sans);letter-spacing:.5px}
.footer ul{position:absolute;top:110px;list-style:none}
.footer li{font:300 11px var(--sans);color:#b8c0cc;height:37px}
.social{position:absolute;top:117px;left:142px;display:flex;gap:9px}
.social i{width:32px;height:32px;border-radius:50%;border:2px solid var(--accent)}
</style>
</head>
<body>

<nav class="nav">
  <a class="active" style="left:266px">HOME</a>
  <a style="left:346px">ABOUT US</a>
  <a style="left:448px">SERVICES</a>
  <div class="nav-brand"><i class="mark"></i><span>MENTORLOFT</span></div>
  <a style="left:697px">CASE STUDIES</a>
  <a style="left:823px">BLOG</a>
  <a style="left:900px">CONTACT</a>
</nav>

<section class="abs hero" role="img" aria-label="Panorama photo of a climber with raised arms on a mountain peak above a sea of clouds at sunrise"></section>
<h1 class="abs center serif" style="top:270px;font-size:56px;line-height:60px;color:#fff">Be a Leader And<br>Define Reality</h1>
<p class="abs center" style="top:407px;color:#fff;font:400 14px var(--sans);letter-spacing:4.5px">HELPING YOU REACH YOUR <b style="font-weight:600">TRUE POTENTIAL</b></p>
<div class="abs dots"><i></i><i></i><i></i><i></i><i></i></div>

<section>
  <div class="abs about-panel"></div>
  <div class="abs about-photo" role="img" aria-label="Photo of colleagues meeting in a bright office lounge"></div>
  <div class="rule" style="left:545px;top:811px"></div>
  <div class="abs eyebrow" style="left:545px;top:826px">About us</div>
  <h2 class="abs serif" style="left:545px;top:848px;font-size:38px;line-height:44px">Turinig Your Carrer<br>Into Prosperity</h2>
  <p class="abs body-text" style="left:545px;top:950px;width:480px">Lorem Ipsum is simply dummy text of the printing industry. Lorem Ipsum has been the industry's standard dummy text ever since the 1500s, when an unknown printer took a galley of type and scrambled it to make a type specimen book.</p>
  <div class="btn" style="left:545px;top:1027px;width:149px;height:41px">Know more</div>
</section>

<div class="rule" style="left:560px;top:1184px"></div>
<div class="abs eyebrow center" style="top:1197px">Our services</div>
<h2 class="abs serif center" style="top:1215px;font-size:38px">What We Offer</h2>

<section class="abs services">
  <div class="card" style="left:0">
    <svg width="60" height="60" viewBox="0 0 60 60" fill="none" stroke="#222" stroke-width="2"><rect x="8" y="4" width="44" height="52" rx="3"/><rect x="16" y="12" width="8" height="8"/><rect x="36" y="12" width="8" height="8"/><rect x="26" y="24" width="8" height="8"/><path d="M20 20v18h10M40 20v18H30v10"/></svg>
    <h3>Leadership<br>Development</h3>
    <p class="body-text">Lorem Ipsum has been the industry's standard dummy text ever since the 1500s, when an unknown printer took a galley of type and scrambled it to make a type specimen book.</p>
    <div class="plus">+</div>
  </div>
  <div class="card active" style="left:300px">
    <svg width="60" height="60" viewBox="0 0 60 60" fill="none" stroke="#222" stroke-width="2"><circle cx="18" cy="20" r="6"/><circle cx="42" cy="14" r="6"/><path d="M6 44c0-8 5-14 12-14s12 6 12 14M30 38c0-10 5-16 12-16s12 6 12 16M4 44h52v8H4z"/></svg>
    <h3>One-on-one<br>Coaching</h3>
    <p class="body-text">Lorem Ipsum has been the industry's standard dummy text ever since the 1500s, when an unknown printer took a galley of type and scrambled it to make a type specimen book.</p>
    <div class="plus">+</div>
  </div>
  <div class="card" style="left:600px">
    <svg width="60" height="60" viewBox="0 0 60 60" fill="none" stroke="#222" stroke-width="2"><circle cx="30" cy="30" r="14"/><path d="M22 6v14M30 4v14M38 6v14M8 42l14-6M52 42l-14-6M22 54v-10M38 54v-10"/></svg>
    <h3>Team<br>Building</h3>
    <p class="body-text">Lorem Ipsum has been the industry's standard dummy text ever since the 1500s, when an unknown printer took a galley of type and scrambled it to make a type specimen book.</p>
    <div class="plus">+</div>
  </div>
  <div class="card" style="left:900px;border-right:none">
    <svg width="60" height="60" viewBox="0 0 60 60" fill="none" stroke="#222" stroke-width="2"><path d="M10 10h14a6 6 0 0 1 12 0h14v14a6 6 0 0 0 0 12v14H36a6 6 0 0 0-12 0H10V36a6 6 0 0 1 0-12z"/><path d="M30 10v40M10 30h40"/></svg>
    <h3>Workplace<br>Solutions</h3>
    <p class="body-text">Lorem Ipsum has been the industry's standard dummy text ever since the 1500s, when an unknown printer took a galley of type and scrambled it to make a type specimen book.</p>
    <div class="plus">+</div>
  </div>
</section>

<section class="abs banner" role="img" aria-label="Photo of a person walking up a curved staircase in warm light"></section>
<div class="rule" style="left:560px;top:1758px;background:#fff"></div>
<h2 class="abs serif center" style="top:1776px;font-size:40px;line-height:49px;color:#fff">A world-class coaching dedicated to<br>delivering world-class solutions</h2>
<p class="abs center" style="top:1886px;font:300 11px/19px var(--sans);color:#fff">Lorem Ipsum is simply dummy text of the printing and typesetting industry. Lorem Ipsum has been the industry's<br>standard dummy text ever since the 1500s, when an unknown printer took a galley of type.</p>
<div class="btn" style="left:525px;top:1953px;width:150px;height:39px">Get started</div>

<section>
  <div class="rule" style="left:560px;top:2151px"></div>
  <div class="abs eyebrow center" style="top:2164px">Blog</div>
  <h2 class="abs serif center" style="top:2182px;font-size:38px">About Current Topics</h2>

  <div class="blog-img" style="left:199px;top:2258px;height:205px;background:linear-gradient(180deg,#bfc8cf,#7c8a86 50%,#5d7a3e)" role="img" aria-label="Photo of a hiker looking at rocky mountain peaks"></div>
  <div class="blog-card" style="left:207px;top:2473px;height:184px">
    <h4>Lorem Ipsum is simply dummy text of the printing industry.</h4>
    <div class="date">&#9635; June 21 2020</div>
    <p>Lorem Ipsum is simply dummy text of the printing and typesetting industry. Lorem Ipsum has been...</p>
    <a>LEARN MORE &rsaquo;</a>
  </div>

  <div class="blog-card" style="left:476px;top:2258px;height:182px">
    <h4>Lorem Ipsum is simply dummy text of the printing industry.</h4>
    <div class="date">&#9635; June 21 2020</div>
    <p>Lorem Ipsum is simply dummy text of the printing and typesetting industry. Lorem Ipsum has been...</p>
    <a>LEARN MORE &rsaquo;</a>
  </div>
  <div class="blog-img" style="left:469px;top:2450px;height:207px;background:linear-gradient(160deg,#d8dce0,#b03a2e 50%,#8a2a22 70%,#c9ccd0)" role="img" aria-label="Overhead photo of two people talking in red armchairs"></div>

  <div class="blog-img" style="left:739px;top:2258px;height:205px;background:linear-gradient(180deg,#8fa2b8,#5a5a4a 55%,#3a2e24)" role="img" aria-label="Photo of a city skyline at dusk"></div>
  <div class="blog-card" style="left:747px;top:2473px;height:184px">
    <h4>Lorem Ipsum is simply dummy text of the printing industry.</h4>
    <div class="date">&#9635; June 21 2020</div>
    <p>Lorem Ipsum is simply dummy text of the printing and typesetting industry. Lorem Ipsum has been...</p>
    <a>LEARN MORE &rsaquo;</a>
  </div>

  <div class="btn" style="left:525px;top:2695px;width:150px;height:40px">View all blog</div>
</section>

<section class="abs case" role="img" aria-label="Misty photo of a wooden pier over calm water"></section>
<div class="abs case-panel">
  <div class="eyebrow" style="font-size:14px">Case study</div>
  <h2 class="serif" style="font-size:38px;margin-top:4px">XYZ Software Solutions</h2>
  <p class="body-text" style="margin-top:12px;width:470px">Lorem Ipsum is simply dummy text of the printing and typesetting industry. Lorem Ipsum has been the industry's standard dummy text ever since the 1500s, when an unknown printer took a galley of type and scrambled it to make a type specimen book. It has survived not only five centuries, but also the leap into electronic type-setting, remaining essentially unchanged.</p>
</div>
<div class="btn" style="left:187px;top:3206px;width:150px;height:41px">View case study</div>
<div class="abs case-photo" role="img" aria-label="Photo of an empty boardroom with a long table and chairs"></div>

<section>
  <div class="abs contact-side"></div>
  <div class="abs brand-line" style="left:88px;top:3460px"><i></i>MENTORLOFT</div>
  <div class="abs info-label" style="left:88px;top:3530px">Give us a call</div>
  <div class="abs info-val" style="left:88px;top:3546px">01 7384 2956</div>
  <div class="abs info-label" style="left:88px;top:3606px">Send us an email</div>
  <div class="abs info-val" style="left:88px;top:3622px">hello@mentorloft.com</div>
  <div class="abs info-label" style="left:88px;top:3684px">Where to find us?</div>
  <div class="abs info-val" style="left:88px;top:3700px;text-decoration:none;line-height:18px">48 Linden Row<br>Brookfield BR4 9TX</div>

  <div class="abs eyebrow" style="left:538px;top:3432px;font-size:14px">Contact us</div>
  <h2 class="abs serif" style="left:538px;top:3452px;font-size:38px">Send A Message</h2>
  <div class="field" style="left:538px;top:3532px;width:261px">Name</div>
  <div class="field" style="left:849px;top:3532px;width:264px">Last Name</div>
  <div class="field" style="left:538px;top:3584px;width:261px">Email *</div>
  <div class="field" style="left:849px;top:3584px;width:264px">Phone *</div>
  <div class="field" style="left:538px;top:3638px;width:575px;height:61px">Message</div>
  <div class="btn" style="left:543px;top:3723px;width:119px;height:41px;background:var(--navy)">Send now</div>
</section>

<footer class="abs footer">
  <div class="abs" style="left:88px;top:78px;display:flex;align-items:center;gap:8px;font:400 20px var(--sans);letter-spacing:2px"><i style="width:20px;height:20px;background:var(--accent)"></i>MENTORLOFT</div>
  <div class="social"><i></i><i></i><i></i></div>

  <h5 style="left:413px">SITEMAP</h5>
  <ul style="left:413px"><li>About Us</li><li>Case Studies</li><li>Blog</li><li>Contact Us</li></ul>

  <h5 style="left:614px">SERVICES</h5>
  <ul style="left:614px"><li>Leadership Development</li><li>One-On-One Coaching</li><li>Team Building</li><li>Workplace Solutions</li></ul>

  <h5 style="left:871px">NEWSLETTER SIGNUP</h5>
  <p class="abs" style="left:871px;top:110px;font:300 11px/18px var(--sans);color:#b8c0cc;width:220px">Sign up for weekly insights, delivered straight to your inbox</p>
  <div class="abs" style="left:871px;top:169px;width:241px;height:34px;background:#fff;color:#999;font:300 10px/34px var(--sans);padding-left:14px">Entre Your Email Address</div>
  <div class="btn" style="left:871px;top:218px;width:135px;height:35px">Subscribe</div>

  <p class="abs" style="left:88px;top:342px;font:400 10px var(--sans)">Copyright © 2020. Mentorloft. All rights reserved | <u>Privacy Policy</u> | <u>Terms &amp; Conditions</u></p>
  <div class="abs" style="left:1061px;top:323px;width:50px;height:50px;border-radius:50%;border:2px solid #fff;display:flex;align-items:center;justify-content:center">
    <svg width="14" height="16" viewBox="0 0 14 16" fill="none" stroke="#fff" stroke-width="2"><path d="M7 15V2M2 7l5-5 5 5"/></svg>
  </div>
</footer>

</body>
</html>
```